New Business Card for Innovative Tool Company

We need a new design of business card for our florida based tool manufacturing company. I will attach 2 files that we use for our logo, use whichever you feel works best for the card. Main colours are as per logo, and we can use different shades of black/white/grey for the background.

Contact Information for Business Card

Name/Jobtitle/cell
Corvalen Tools
Suite 212c
4316 Marrowdale Pkw
Orlando, FL32847
USA
name@corvaleninc.example
www.corvaleninc.example

Font styles to use
Sans Serif

Colors

Designer to choose colors to be used in the design.

Requirements
Must have
• Icons for Plazaro, Chirpet, Snapvale, Findlo & Vidstream

```html
<!DOCTYPE html>
<html lang="en">
<head>
<meta charset="utf-8">
<title>Corvalen Tools – Business Card</title>
<link rel="stylesheet" href="https://fonts.googleapis.com/css2?family=Roboto:wght@400;700&display=swap">
<style>
  :root {
    --bg: #e9e7e3;
    --ink: #111111;
    --steel: #5b5c5e;
    --steel-dark: #4e4f51;
    --signal: #f7ec3d;
    --olive: #77723c;
    --white: #f2f2f2;
  }
  * { box-sizing: border-box; margin: 0; padding: 0; }
  html, body { width: 1200px; height: 886px; overflow: hidden; }
  body {
    background: var(--bg);
    font-family: "Roboto", Arial, sans-serif;
    display: flex; align-items: center; justify-content: center; gap: 40px;
  }
  .card {
    position: relative; width: 540px; height: 309px; overflow: hidden;
    box-shadow: 0 10px 28px rgba(0,0,0,.25);
  }
  /* front */
  .card-front { background: var(--ink); }
  .band { position: absolute; left: 0; right: 0; bottom: 0; height: 96px; display: flex; }
  .band-address { width: 240px; background: var(--signal); padding: 18px 0 0 26px;
    color: var(--ink); font-size: 12.5px; line-height: 1.45; }
  .band-contact { flex: 1; background: var(--steel); padding: 16px 20px 0 0;
    color: var(--white); font-size: 12.5px; line-height: 1.55; text-align: right; }
  .contact-line { display: flex; justify-content: flex-end; align-items: center; gap: 8px; }
  .contact-line svg { width: 12px; height: 12px; flex: none; }
  .seal {
    position: absolute; left: 194px; top: 169px; width: 92px; height: 92px;
    border-radius: 50%; background: var(--ink); border: 3px solid var(--signal);
    display: flex; align-items: center; justify-content: center;
    color: var(--signal); font-weight: 700; font-size: 13px;
  }
  .brand { position: absolute; left: 34px; top: 120px; display: flex; align-items: center; gap: 12px; }
  .brand-dot { width: 34px; height: 34px; border-radius: 50%; border: 2px solid var(--signal); }
  .brand-name { color: var(--signal); font-weight: 700; font-size: 26px; letter-spacing: 1px; text-transform: uppercase; }
  .person { position: absolute; right: 30px; top: 30px; text-align: right; }
  .person-name { color: var(--signal); font-weight: 700; font-size: 17px; }
  .person-title { color: var(--white); font-size: 12px; margin-top: 2px; }
  /* back */
  .card-back { background: var(--steel); }
  .back-ring { position: absolute; left: 170px; top: 18px; width: 200px; height: 200px;
    border-radius: 50%; border: 2px solid var(--olive); }
  .back-brand { position: absolute; left: 0; right: 0; top: 206px; text-align: center;
    color: var(--signal); font-weight: 700; font-size: 24px; letter-spacing: 1px; text-transform: uppercase; }
  .social { position: absolute; left: 0; right: 0; top: 252px; display: flex; justify-content: center; gap: 22px; }
  .social-item { display: flex; align-items: center; gap: 5px; color: var(--signal); font-size: 10.5px; }
  .social-dot { width: 14px; height: 14px; border-radius: 50%; border: 1.5px solid var(--signal); }
</style>
</head>
<body>
  <section class="card card-front" aria-label="Business card front">
    <div class="person">
      <div class="person-name">DANAKELLER</div>
      <div class="person-title">CEO/FOUNDER</div>
    </div>
    <div class="brand">
      <span class="brand-dot"></span>
      <span class="brand-name">Corvalen Tools</span>
    </div>
    <div class="band">
      <div class="band-address">
        Corvalen Tools, Suite 212c<br>
        4316 Marrowdale Pkw<br>
        Orlando, FL32847 USA
      </div>
      <div class="band-contact">
        <div class="contact-line">555 014 2290
          <svg viewBox="0 0 12 12"><rect x="3" y="1" width="6" height="10" rx="1" fill="none" stroke="var(--signal)" stroke-width="1.3"/></svg></div>
        <div class="contact-line">name@corvaleninc.example
          <svg viewBox="0 0 12 12"><rect x="1" y="2.5" width="10" height="7" fill="var(--signal)"/><path d="M1 2.5l5 4 5-4" fill="none" stroke="var(--steel)" stroke-width="1"/></svg></div>
        <div class="contact-line">www.corvaleninc.example
          <svg viewBox="0 0 12 12"><circle cx="6" cy="6" r="5" fill="var(--signal)"/><path d="M1 6h10M6 1v10" stroke="var(--steel)" stroke-width="1"/></svg></div>
      </div>
    </div>
    <div class="seal">Corvalen</div>
  </section>

  <section class="card card-back" aria-label="Business card back">
    <div class="back-ring"></div>
    <div class="back-brand">Corvalen Tools</div>
    <div class="social">
      <span class="social-item"><span class="social-dot"></span>Plazaro</span>
      <span class="social-item"><span class="social-dot"></span>Chirpet</span>
      <span class="social-item"><span class="social-dot"></span>Snapvale</span>
      <span class="social-item"><span class="social-dot"></span>Findlo</span>
      <span class="social-item"><span class="social-dot"></span>Vidstream</span>
    </div>
  </section>
</body>
</html>
```